Company profile urgent

Hi, I had my designer fail to deliver and I am looking for urgent designers job. Needs to go to print tomorrow the latest. I need company profile designed and finished, I do have a start of the project but did not like the overall design as it was too simple and not something I would asking for. This needs to be a great job and we are willing to pay for the right job.

This is pretty much a folded brochure as you will see from the document that is attached. On the front side do not remove LOGO from the actual position as it must stay there for the purposes of the cover that is going over and it has a whole for the logo where it is. Also, the pages are set as it should be so do not change the order of the pages, only the design, feel and look. This is for a travel company needs to look expensive, upscale, vip and must have clean design.

Needs to be done:

.

Needs to be done:

1) Get the design more attractive and modern. Not looking for cheap but high quality material.
2) As you can see we are tryin to present 4 products in the brochure that we do and this will be a folded brochure.
3) Infographics, especially the table ''when to travel'' needs updates and more style
4) This design is very steril, we are looking for clean and modern design
5) On the front page add Company profile text somewhere and add any design on home page is welcome BUT logo must stay where is
6) Please send final print ready documents as well as editable so we can move the logo if needed as it must fit the whole on a brochure holder
7) Last page with contacts very poorly done by my designer, needs upgrade with maybe infographics for phone, email web etc... ideas welcome
8) if you need more photos at the end is link to photo bank

Ideas welcome! Again we need it fast and clean.

Photo bank:
https://files.orvenbox.example/f/q7Lm2Xa9Tz4Pb8Kd

Designes that we linked: https://layoutmarket.example/item/company-profile-square-brochure/48817203?s_rank=8
https://layoutmarket.example/item/company-profile_square/51390628?s_rank=32
https://layoutmarket.example/item/square-brochure/53704916?s_rank=52

This is our webiste so you get the feeling of the colors: www.selvotrips.example

Important: Do not change text, or change pages, everything is as it should be just needs upgradede design! Logo on the first page must stay on the position as is.

Photo bank:

Target Market(s)

We are travel supplier targeting travel agents and travel companies

Industry/Entity Type

Travel Industry

Font styles to use
Serif
Sans Serif

Requirements
Must have
• https://files.orvenbox.example/f/w3Hn6Rc1Ys5Qe2Jv
Nice to have
• Cool design: https://layoutmarket.example/item/business-solution-brochure-template/46182057?s_rank=3
• Cool design 2: https://layoutmarket.example/item/travel-agency-catalog-brochure/47269815?s_rank=6
Should not have
• Do not change the dimensions. You have the design attached, indd file. Needs work and update.

```html
<!DOCTYPE html>
<html lang="en">
<head>
<meta charset="utf-8">
<title>Selvo Trips – Company Profile Cover</title>
<link rel="stylesheet" href="https://fonts.googleapis.com/css2?family=Open+Sans:wght@300;400;700;800&display=swap">
<style>
  :root {
    --brand-red: #a30f22;
    --brand-red-deep: #7e1620;
    --paper: #f4f4f4;
    --ink-white: #ffffff;
    --tab-dark: #1d1d1d;
    --sea-deep: #2f6f8f;
    --sea-light: #7fc8dc;
    --sky-haze: #e9d7d2;
  }
  * { margin: 0; padding: 0; box-sizing: border-box; }
  html, body { width: 1200px; height: 900px; overflow: hidden; background: var(--paper); }
  body { font-family: "Open Sans", Arial, sans-serif; }

  .cover { position: relative; width: 1200px; height: 900px; overflow: hidden;
    background: linear-gradient(160deg, #ffffff 0%, #eeeeee 100%); }
  .cover-art { position: absolute; inset: 0; }

  .brand { position: absolute; left: 150px; top: 70px; color: var(--brand-red);
    font-weight: 800; line-height: 1; }
  .brand-name { display: block; font-size: 92px; letter-spacing: 4px; }
  .brand-sub { display: block; font-size: 26px; letter-spacing: 34px; margin-top: 18px; padding-left: 6px; }

  .tagline { position: absolute; left: 60px; top: 640px; color: var(--ink-white); }
  .tagline-lead { display: block; font-size: 58px; font-weight: 800; line-height: 1; }
  .tagline-rest { display: block; font-size: 40px; font-weight: 300; line-height: 1.15; letter-spacing: 1px; }

  .web-link { position: absolute; left: 60px; top: 782px; display: flex; align-items: center; gap: 12px;
    color: var(--ink-white); font-size: 26px; font-weight: 400; }
  .web-link svg { width: 22px; height: 22px; }

  .edge-tab { position: absolute; left: 0; top: 752px; width: 34px; height: 46px; background: var(--tab-dark); }
</style>
</head>
<body>
<main class="cover">
  <svg class="cover-art" viewBox="0 0 1200 900" width="1200" height="900">
    <defs>
      <linearGradient id="red-band" x1="0" y1="0" x2="1" y2="1">
        <stop offset="0" stop-color="var(--brand-red)"/>
        <stop offset="1" stop-color="var(--brand-red-deep)"/>
      </linearGradient>
      <linearGradient id="sea-photo" x1="0" y1="0" x2="1" y2="1">
        <stop offset="0" stop-color="var(--sky-haze)"/>
        <stop offset="0.35" stop-color="var(--sea-light)"/>
        <stop offset="1" stop-color="var(--sea-deep)"/>
      </linearGradient>
      <linearGradient id="waterfall-photo" x1="0" y1="0" x2="1" y2="1">
        <stop offset="0" stop-color="#4f7b2c"/>
        <stop offset="0.5" stop-color="#c9d2c8"/>
        <stop offset="1" stop-color="#3f5e24"/>
      </linearGradient>
      <linearGradient id="oldtown-photo" x1="0" y1="0" x2="1" y2="1">
        <stop offset="0" stop-color="#2e6e98"/>
        <stop offset="0.5" stop-color="#b9704e"/>
        <stop offset="1" stop-color="#6d8a4a"/>
      </linearGradient>
      <linearGradient id="islands-photo" x1="0" y1="0" x2="0" y2="1">
        <stop offset="0" stop-color="#9cc6e6"/>
        <stop offset="0.45" stop-color="#1f5fa8"/>
        <stop offset="1" stop-color="#4f8a3a"/>
      </linearGradient>
    </defs>

    <polygon class="red-band" points="0,270 600,900 0,900" fill="url(#red-band)"/>

    <polygon class="hero-photo" role="img" aria-label="Photo: white motor yacht speeding across turquoise sea, aerial view"
      points="850,0 1200,0 1200,900 640,900 470,430" fill="url(#sea-photo)"/>

    <g class="photo-tile" transform="rotate(-28 395 355)">
      <rect role="img" aria-label="Photo: forest waterfall over mossy rocks" x="320" y="280" width="150" height="150" fill="url(#waterfall-photo)"/>
      <rect x="332" y="292" width="126" height="126" fill="none" stroke="#fff" stroke-width="1.5"/>
    </g>
    <g class="photo-tile" transform="rotate(-28 560 560)">
      <rect role="img" aria-label="Photo: walled old town on the coast" x="440" y="440" width="240" height="240" fill="url(#oldtown-photo)"/>
      <rect x="456" y="456" width="208" height="208" fill="none" stroke="#fff" stroke-width="1.5"/>
    </g>
    <g class="photo-tile" transform="rotate(-28 690 800)">
      <rect role="img" aria-label="Photo: green islands and deep blue bay" x="565" y="675" width="250" height="250" fill="url(#islands-photo)"/>
      <rect x="581" y="691" width="218" height="218" fill="none" stroke="#fff" stroke-width="1.5"/>
    </g>
  </svg>

  <div class="brand">
    <span class="brand-name">SELVO</span>
    <span class="brand-sub">TRIPS</span>
  </div>

  <h1 class="tagline">
    <span class="tagline-lead">YOUR</span>
    <span class="tagline-rest">TAGLINE HERE</span>
  </h1>

  <div class="edge-tab"></div>

  <p class="web-link">
    <svg viewBox="0 0 24 24" fill="none" stroke="currentColor" stroke-width="1.6" aria-hidden="true">
      <circle cx="12" cy="12" r="10"/><ellipse cx="12" cy="12" rx="4.5" ry="10"/>
      <line x1="2" y1="12" x2="22" y2="12"/>
    </svg>
    www.yoursite.example
  </p>
</main>
</body>
</html>
```